Estate Planning Law Firm opening new branch in Florida

I am an experienced estate planning attorney that recently relocated to Florida. Looking for a banner Ad to place on platforms such as YardLoop, Chatterly and Pixmora to create publicity for firm and new leads.

```html
<!DOCTYPE html>
<html lang="en">
<head>
<meta charset="utf-8">
<title>Serenova Law Firm – Estate Planning & Financial Planning</title>
<link rel="stylesheet" href="https://fonts.googleapis.com/css2?family=Tinos:wght@400;700&family=Montserrat:wght@500&display=swap">
<style>
  :root {
    --navy: #0c1f3c;
    --royal: #0a5aae;
    --teal: #1b6f73;
    --teal-line: #2a8a86;
    --photo-deep: #0e2c52;
    --photo-mid: #1a5693;
    --photo-light: #2a6fae;
    --photo-green: #2f6f7a;
    --suit: #2a3446;
    --white: #ffffff;
  }
  * { margin: 0; padding: 0; box-sizing: border-box; }
  html, body { width: 1200px; height: 675px; overflow: hidden; background: var(--navy); }
  .banner { position: relative; width: 1200px; height: 675px; background: var(--navy); overflow: hidden; font-family: "Tinos", "Times New Roman", serif; color: var(--white); }
  .shapes { position: absolute; inset: 0; }
  .brand { position: absolute; left: 97px; top: 52px; width: 258px; text-align: center; }
  .brand-name { font-weight: 700; font-size: 52px; line-height: 52px; letter-spacing: -0.5px; }
  .brand-sub { display: flex; align-items: center; gap: 6px; margin-top: 5px; font-family: "Montserrat", sans-serif; font-weight: 500; font-size: 16px; }
  .brand-sub::before, .brand-sub::after { content: ""; flex: 1; height: 2px; background: var(--teal-line); }
  .headline { position: absolute; left: 38px; top: 252px; }
  .welcome { font-size: 18.5px; letter-spacing: 0.2px; }
  .title { font-weight: 700; font-size: 46px; line-height: 43px; margin-top: 13px; letter-spacing: -0.8px; }
  .tagline { font-size: 24px; margin-top: 10px; }
  .social { position: absolute; left: 40px; top: 490px; display: flex; gap: 16px; list-style: none; }
  .social li { display: flex; align-items: center; gap: 6px; font-size: 14px; }
  .social .dot { width: 31px; height: 31px; border-radius: 50%; background: var(--white); border: 2px solid var(--royal); box-shadow: 0 0 0 1.5px var(--white); }
  .contact { position: absolute; left: 576px; top: 500px; display: flex; align-items: center; font-size: 28px; }
  .contact-item { display: flex; align-items: center; gap: 13px; }
  .contact-item svg { width: 30px; height: 30px; }
  .divider { width: 2px; height: 68px; background: var(--white); margin: 0 18px 0 30px; }
</style>
</head>
<body>
<div class="banner">
  <svg class="shapes" width="1200" height="675" viewBox="0 0 1200 675">
    <defs>
      <linearGradient id="buildingTone" x1="0" y1="0" x2="0.3" y2="1">
        <stop offset="0" stop-color="var(--photo-light)"/>
        <stop offset="0.45" stop-color="var(--photo-mid)"/>
        <stop offset="0.75" stop-color="var(--photo-green)"/>
        <stop offset="1" stop-color="var(--photo-deep)"/>
      </linearGradient>
      <radialGradient id="figureTone" cx="0.72" cy="0.75" r="0.45">
        <stop offset="0" stop-color="var(--suit)" stop-opacity="0.85"/>
        <stop offset="0.6" stop-color="var(--suit)" stop-opacity="0.4"/>
        <stop offset="1" stop-color="var(--suit)" stop-opacity="0"/>
      </radialGradient>
      <clipPath id="photoClip">
        <path d="M655 44 H1200 V632 H270 Q250 632 262 612 L640 56 Q648 44 655 44 Z"/>
      </clipPath>
    </defs>
    <g role="img" aria-label="Photo of a smiling attorney in a dark suit and patterned tie in front of a classic stone office building, tinted blue" clip-path="url(#photoClip)">
      <rect x="250" y="44" width="950" height="588" fill="url(#buildingTone)"/>
      <rect x="250" y="44" width="950" height="588" fill="url(#figureTone)"/>
    </g>
    <path d="M0 179 H652 Q670 179 660 196 L452 524 Q444 536 430 536 H0 Z" fill="var(--royal)"/>
    <path d="M612 470 H1200 V603 H518 Q503 603 512 590 L598 478 Q604 470 612 470 Z" fill="var(--teal)"/>
  </svg>

  <header class="brand">
    <div class="brand-name">SERENOVA</div>
    <div class="brand-sub">LAW FIRM, PLLC</div>
  </header>

  <section class="headline">
    <p class="welcome">WELCOME TO SERENOVA</p>
    <h1 class="title">ESTATE PLANNING &amp;<br>FINANCIAL PLANNING</h1>
    <p class="tagline">UNDER ONE ROOF</p>
  </section>

  <ul class="social">
    <li><span class="dot"></span>Chatterly</li>
    <li><span class="dot"></span>Linkora</li>
    <li><span class="dot"></span>Blog</li>
  </ul>

  <div class="contact">
    <div class="contact-item">
      <svg viewBox="0 0 30 30" aria-hidden="true"><circle cx="15" cy="15" r="14" fill="var(--white)"/><circle cx="15" cy="15" r="11.5" fill="none" stroke="var(--teal)" stroke-width="1"/><rect x="8.5" y="10.5" width="13" height="9" rx="1" fill="var(--teal)"/><path d="M8.8 11 L15 15.8 L21.2 11" stroke="var(--white)" stroke-width="1.2" fill="none"/></svg>
      <span>support@serenova.law</span>
    </div>
    <div class="divider"></div>
    <div class="contact-item">
      <svg viewBox="0 0 30 30" aria-hidden="true"><circle cx="15" cy="15" r="14" fill="var(--white)"/><circle cx="15" cy="15" r="11.5" fill="none" stroke="var(--teal)" stroke-width="1"/><path d="M11 8.5 L13.5 8 L15 11.5 L13.3 13 Q14.5 15.8 17 16.8 L18.5 15 L22 16.5 L21.5 19 Q20.5 21.5 17.5 20.8 Q11 18.5 9 12.5 Q8.5 9.5 11 8.5 Z" fill="var(--teal)"/></svg>
      <span>[555]014-2290</span>
    </div>
  </div>
</div>
</body>
</html>
```